ParlaShift - Brighter relocation answers, Now!

Hello,
I'd like to update, re-vamp, and re-tool this current power point presentation with slightly more professional appearance as well as more accurately reflect the website -parlashift.com- color scheme and sleek design scheme. Please see attached.
We at ParlaShift pride ourselves on seeking to rework an archaic business into something progressive, cost effective, more reliable, and easily accessible in todays fast growing market that has only gotten more expensive, more costly and less indirect over the last couple years.

Target Market(s)

New updated and hassle free moving opportunities no matter how large or how small in a market that begs for a change

Industry/Entity Type

Logistics/Moving

Requirements
Must have
• The current color scheme from the -parlashift.com- website as well as the inclusion of the current data on the sample power point presentation provided but with updated graphics

```html
<!DOCTYPE html>
<html lang="en">
<head>
<meta charset="utf-8">
<title>ParlaShift – Moving For The Next Generation</title>
<link href="https://fonts.googleapis.com/css2?family=Poppins:wght@300;400;500;600;700;800&display=swap" rel="stylesheet">
<style>
  :root{
    --brand-blue:#2a63e6;
    --ink:#111111;
    --body:#2b2b2b;
    --gold:#f3c35a;
    --gold-deep:#c9a24e;
    --sidebar:#2c2c2e;
    --rule:#ececec;
    --white:#ffffff;
  }
  *{box-sizing:border-box;margin:0;padding:0}
  html,body{width:1200px;height:2400px;overflow:hidden;background:var(--white)}
  body{position:relative;font-family:'Poppins',sans-serif;color:var(--body)}
  .abs{position:absolute}

  /* header */
  .brand{left:109px;top:40px;display:flex;align-items:center;gap:14px}
  .brand-square{width:30px;height:30px;background:var(--brand-blue)}
  .brand-name{font-size:46px;font-weight:600;color:var(--brand-blue);letter-spacing:1px;line-height:1}

  /* hero */
  .hero{left:67px;top:135px;width:1066px;height:464px;
    background:linear-gradient(100deg,#2d3033 0%,#4b4b4a 35%,#6a6058 60%,#8b7b6d 100%)}
  .hero-title{left:40px;top:68px;font-size:65px;font-weight:700;color:var(--white);line-height:80px}
  .hero-url{left:40px;top:385px;font-size:26px;font-weight:400;color:var(--white)}

  /* slides */
  .slide{left:67px;width:1066px;height:600px;overflow:hidden}
  .sidebar{left:0;top:0;width:42px;height:100%;
    background:linear-gradient(180deg,var(--sidebar) 0%,var(--sidebar) 55%,#6b5a35 80%,var(--gold-deep) 100%)}
  .side-mark{left:12px;top:22px;width:18px;height:18px;background:var(--brand-blue)}
  .side-url{left:21px;top:250px;transform:translateX(-50%) rotate(-90deg);transform-origin:center;
    font-size:14px;letter-spacing:5px;color:#cfcfcf;white-space:nowrap;font-weight:300}
  .side-num{left:0;width:42px;bottom:28px;text-align:center;font-size:11px;color:#fff3d0}

  /* about */
  .about{top:599px}
  .about-photo{left:42px;top:0;width:447px;height:600px;
    background:linear-gradient(160deg,#d9d5cf 0%,#e8e3dc 45%,#cdb79a 100%)}
  .about-title{left:533px;top:145px;font-size:43px;font-weight:700;color:var(--ink)}
  .about-copy{left:533px;top:222px;width:490px;font-size:16.5px;line-height:25.6px;color:var(--body)}
  .about-copy p+p{margin-top:25.6px}

  /* vision */
  .vision{top:1199px}
  .vision-photo{left:42px;top:0;width:1024px;height:301px;
    background:linear-gradient(180deg,#5e5a56 0%,#7a6c5d 55%,#8f7c66 100%)}
  .vision-title{left:42px;width:1024px;top:38px;text-align:center;font-size:43px;font-weight:700;color:var(--white)}
  .vision-sub{left:42px;width:1024px;top:102px;text-align:center;font-size:17px;color:var(--gold);font-weight:400}
  .card-wrap{top:198px;width:302px;height:362px;filter:drop-shadow(0 10px 18px rgba(0,0,0,.12))}
  .card{width:100%;height:100%;background:var(--white);padding:52px 26px 0 28px;
    clip-path:polygon(0 0,calc(100% - 48px) 0,100% 48px,100% 100%,0 100%)}
  .card-title{font-size:27px;font-weight:700;color:var(--ink);line-height:1}
  .card-icon{position:absolute;right:30px;top:24px}
  .card-lead{margin-top:16px;font-size:18px;line-height:21px;color:var(--brand-blue)}
  .card-lead b{font-weight:700}
  .card-body{margin-top:16px;font-size:14.5px;line-height:20.5px;color:var(--body)}

  /* problems */
  .problems{top:1799px;height:601px}
  .problems-title{left:74px;top:40px;font-size:41px;font-weight:700;line-height:48px;color:var(--ink)}
  .timeline{left:98px;top:369px;width:968px;height:10px;background:var(--rule)}
  .problem{top:223px;width:240px}
  .problem-num{margin-top:6px;font-size:34px;font-weight:700;color:var(--brand-blue);line-height:1}
  .dot{position:absolute;top:142px;left:2px;width:26px;height:26px;border-radius:50%;background:var(--white);border:6px solid var(--gold)}
  .problem-head{position:absolute;top:182px;left:0;font-size:22px;font-weight:800;color:var(--brand-blue);letter-spacing:.3px;white-space:nowrap}
  .problem-body{position:absolute;top:222px;left:0;width:190px;font-size:14px;line-height:19px;color:var(--body)}
  .problem-body b{color:var(--brand-blue);font-size:17px;font-weight:700}
</style>
</head>
<body>

<header class="abs brand">
  <span class="brand-square" aria-hidden="true"></span>
  <span class="brand-name">ParlaShift</span>
</header>

<section class="abs hero" role="img" aria-label="Photo of a happy couple dancing among moving boxes in a new home">
  <h1 class="abs hero-title">Moving For<br>The Next<br>Generation</h1>
  <div class="abs hero-url">www.parlashift.com</div>
</section>

<section class="abs slide about">
  <div class="abs sidebar">
    <span class="abs side-mark"></span>
    <span class="abs side-url">parlashift.com</span>
    <span class="abs side-num">2</span>
  </div>
  <div class="abs about-photo" role="img" aria-label="Photo of a smiling couple carrying cardboard boxes and a plant into a bright room"></div>
  <h2 class="abs about-title">About Us</h2>
  <div class="abs about-copy">
    <p>ParlaShift is the next logical evolution in professional moving. Professional moving clients have battled soaring prices, acute capacity problems and deteriorating service levels.</p>
    <p>ParlaShift was founded by lifelong moving professionals who have developed the answer to better moving services. Poised as THE industry disruptor, we deliver faster, offer guaranteed prices and even offer no credit check financing options. We are a technology first organization using proprietary software to deliver moving's best service experience.</p>
  </div>
</section>

<section class="abs slide vision">
  <div class="abs vision-photo" role="img" aria-label="Photo of a child playing with a cardboard tube among stacked moving boxes"></div>
  <div class="abs sidebar">
    <span class="abs side-mark"></span>
    <span class="abs side-url">parlashift.com</span>
    <span class="abs side-num">3</span>
  </div>
  <h2 class="abs vision-title">PARLASHIFT Vision</h2>
  <p class="abs vision-sub">The traditional moving industry is broken, outdated, inefficient, and unable to change.</p>

  <div class="abs card-wrap" style="left:86px">
    <article class="card">
      <svg class="card-icon" width="52" height="52" viewBox="0 0 52 52" aria-hidden="true">
        <ellipse cx="26" cy="32" rx="22" ry="12" fill="none" stroke="#1f2d4a" stroke-width="2.5"/>
        <circle cx="26" cy="32" r="7" fill="#3f8ff0" stroke="#1f2d4a" stroke-width="2"/>
        <path d="M14 16 L14 4 M10 8 L14 4 L18 8 M26 14 L26 2 M22 6 L26 2 L30 6 M38 16 L38 4 M34 8 L38 4 L42 8" stroke="#3f8ff0" stroke-width="2.5" fill="none"/>
      </svg>
      <h3 class="card-title">Our Vision</h3>
      <p class="card-lead">Revolutionize an <b>$86B</b> industry by providing great value to everyone involved</p>
      <p class="card-body">ParlaShift Customers - Consumers, Movers, Corporate Clients, and Relocation Management Companies all receive better value with ParlaShift than anywhere else.</p>
    </article>
  </div>

  <div class="abs card-wrap" style="left:412px">
    <article class="card">
      <svg class="card-icon" width="56" height="56" viewBox="0 0 56 56" aria-hidden="true">
        <circle cx="26" cy="30" r="22" fill="#fde7a6" stroke="#1f2d4a" stroke-width="2.5"/>
        <circle cx="26" cy="30" r="14" fill="#fff" stroke="#1f2d4a" stroke-width="2.5"/>
        <circle cx="26" cy="30" r="6" fill="#e8473b" stroke="#1f2d4a" stroke-width="2"/>
        <path d="M26 30 L50 6 M44 4 L50 6 L52 12" stroke="#1f2d4a" stroke-width="2.5" fill="none"/>
      </svg>
      <h3 class="card-title">Our Mission</h3>
      <p class="card-lead">Disrupt a sleepy giant of an inefficient industry</p>
      <p class="card-body">ParlaShift's deep understanding of the professional moving industry, supported by extensive market research has set ParlaShift up for ultimate success in disrupting this industry by creating cost-saving efficiencies throughout.</p>
    </article>
  </div>

  <div class="abs card-wrap" style="left:734px">
    <article class="card">
      <svg class="card-icon" width="58" height="54" viewBox="0 0 58 54" aria-hidden="true">
        <circle cx="34" cy="22" r="17" fill="#58b368" stroke="#1f2d4a" stroke-width="2.5"/>
        <path d="M2 42 L22 38 L40 42 L56 34 L56 44 L36 52 L2 50 Z" fill="#f7c9a4" stroke="#1f2d4a" stroke-width="2.5"/>
        <circle cx="42" cy="6" r="4" fill="#e8473b"/>
      </svg>
      <h3 class="card-title">Our Goal</h3>
      <p class="card-lead">Becoming the moving platform of choice</p>
      <p class="card-body" style="margin-top:26px">As ParlaShift's market share grows, the customer acquisition cost and operational cost plummets. This creates even more market penetration, more efficiencies, and exponential growth.</p>
    </article>
  </div>
</section>

<section class="abs slide problems">
  <div class="abs sidebar">
    <span class="abs side-mark"></span>
    <span class="abs side-url">parlashift.com</span>
    <span class="abs side-num">4</span>
  </div>
  <h2 class="abs problems-title">Moving’s<br>Problems</h2>
  <div class="abs timeline"></div>

  <div class="abs problem" style="left:114px">
    <svg width="58" height="62" viewBox="0 0 58 62" aria-hidden="true">
      <circle cx="14" cy="31" r="12" fill="#f3c35a" stroke="#1f2d4a" stroke-width="2.5"/>
      <path d="M26 31 H34 M34 10 V52 M34 10 H40 M34 31 H40 M34 52 H40" stroke="#1f2d4a" stroke-width="2.5" fill="none"/>
      <rect x="40" y="2" width="16" height="16" fill="#d9a866" stroke="#1f2d4a" stroke-width="2"/>
      <rect x="40" y="23" width="16" height="16" fill="#d9a866" stroke="#1f2d4a" stroke-width="2"/>
      <rect x="40" y="44" width="16" height="16" fill="#d9a866" stroke="#1f2d4a" stroke-width="2"/>
    </svg>
    <div class="problem-num">01</div>
    <span class="dot"></span>
    <h3 class="problem-head">COST</h3>
    <p class="problem-body">Moving cost has skyrocketed over the last three years. Charges have increased <b>38%</b> since 2018.</p>
  </div>

  <div class="abs problem" style="left:361px">
    <svg width="58" height="62" viewBox="0 0 58 62" aria-hidden="true">
      <rect x="2" y="2" width="24" height="20" fill="#d9a866" stroke="#1f2d4a" stroke-width="2"/>
      <path d="M8 24 V42 H2 L14 60 L26 42 H20 V24 Z" fill="#58b368" stroke="#1f2d4a" stroke-width="2"/>
      <path d="M44 2 L56 20 H50 V38 H38 V20 H32 Z" fill="#e8473b" stroke="#1f2d4a" stroke-width="2"/>
      <text x="37" y="60" font-family="Poppins,sans-serif" font-size="20" font-weight="700" fill="#58b368">$</text>
    </svg>
    <div class="problem-num">02</div>
    <span class="dot"></span>
    <h3 class="problem-head">CAPACITY</h3>
    <p class="problem-body">Long-haul driver shortages and limited equipment coupled with growing demand has pushed capacity to a crisis state</p>
  </div>

  <div class="abs problem" style="left:608px">
    <svg width="62" height="62" viewBox="0 0 62 62" aria-hidden="true">
      <rect x="6" y="10" width="24" height="20" fill="#d9a866" stroke="#1f2d4a" stroke-width="2"/>
      <circle cx="46" cy="14" r="9" fill="#f3c35a" stroke="#1f2d4a" stroke-width="2"/>
      <path d="M2 34 Q18 30 30 38 L44 44 L52 52 L40 58 L24 50 L2 48 Z" fill="#f7c9a4" stroke="#1f2d4a" stroke-width="2"/>
      <rect x="46" y="46" width="12" height="12" fill="#3f8ff0" stroke="#1f2d4a" stroke-width="2" transform="rotate(40 52 52)"/>
    </svg>
    <div class="problem-num">03</div>
    <span class="dot"></span>
    <h3 class="problem-head">SERVICE</h3>
    <p class="problem-body">Quality labor has been difficult to source and afford. Virtually all RMC’s report a decline in service quality</p>
  </div>

  <div class="abs problem" style="left:856px">
    <svg width="66" height="62" viewBox="0 0 66 62" aria-hidden="true">
      <circle cx="42" cy="22" r="19" fill="#fdf0c6" stroke="#1f2d4a" stroke-width="3"/>
      <path d="M28 36 L6 58" stroke="#3f8ff0" stroke-width="7" stroke-linecap="round"/>
      <path d="M28 36 L6 58" stroke="#1f2d4a" stroke-width="2" stroke-linecap="round"/>
    </svg>
    <div class="problem-num">04</div>
    <span class="dot"></span>
    <h3 class="problem-head">TRANSPARANCY</h3>
    <p class="problem-body">Too many margin layers...van line, agent, driver and help. In addition, charges are convoluted and confusing</p>
  </div>
</section>

</body>
</html>
```